We have a parent company, Summit Harbor Group (SHG), that has other company partners. We are looking for ways to incorporate our SHG logo with our network partners, Beacon Ledger and The Blue Gate. My initial thought is to have SHG as front of card logo, and include The Blue Gate and Beacon Ledger logos on back but I'm open to ideas. Card should include website www.summitharborgrp.example (use for reference). Keywords "Tax Services" "Real Estate" "Insurance" "Investments" "Chief Financial Officer"

Industry/Entity Type

Financial

```html
<!DOCTYPE html>
<html lang="en">
<head>
<meta charset="utf-8">
<title>Summit Harbor Group – Business Card</title>
<link rel="stylesheet" href="https://fonts.googleapis.com/css2?family=Cinzel:wght@500;600&family=Open+Sans:wght@400;600&display=swap">
<style>
  :root {
    --stage: #4b4b4b;
    --card-white: #ffffff;
    --card-grey: #e6e6e6;
    --brand-red: #ec1f2b;
    --brand-blue: #0d55a8;
    --ink: #1f1f1f;
  }
  * { box-sizing: border-box; margin: 0; padding: 0; }
  html, body { width: 1200px; height: 900px; overflow: hidden; }
  body { background: var(--stage); position: relative; font-family: "Open Sans", Arial, sans-serif; }

  .card { position: absolute; top: 306px; height: 272px; overflow: hidden; }
  .card--front { left: 149px; width: 439px; background: var(--card-white); }
  .card--back { left: 608px; width: 441px; background: var(--card-grey); }

  .band { position: absolute; left: 0; width: 100%; }
  .band--top { top: 0; height: 38px; background: var(--brand-red); }
  .band--bottom { bottom: 0; height: 12px; background: var(--brand-blue); }

  .holder { position: absolute; left: 23px; top: 110px; }
  .holder__name {
    font-family: "Cinzel", Georgia, serif; font-weight: 600;
    font-size: 19px; color: var(--brand-blue); letter-spacing: 0.3px; line-height: 1;
  }
  .holder__title { font-size: 12px; color: var(--ink); margin-top: 3px; }

  .contact { position: absolute; left: 23px; top: 156px; list-style: none; }
  .contact li { display: flex; align-items: center; font-size: 12.5px; color: var(--ink); height: 16px; }
  .contact svg { width: 9px; height: 9px; margin-right: 6px; fill: var(--brand-blue); }

  .partner {
    position: absolute; right: 23px;
    font-family: "Cinzel", Georgia, serif; font-weight: 600; line-height: 1; white-space: nowrap;
  }
  .partner--gate { top: 130px; font-size: 15px; color: var(--brand-red); }
  .partner--ledger { top: 186px; font-size: 18px; color: var(--brand-red); }

  .identity {
    position: absolute; left: 0; right: 0; top: 112px;
    display: flex; align-items: center; justify-content: center; gap: 10px;
  }
  .identity__dot { width: 22px; height: 22px; border-radius: 50%; background: var(--brand-red); }
  .identity__name {
    font-family: "Cinzel", Georgia, serif; font-weight: 600;
    font-size: 23px; color: var(--brand-blue); line-height: 1;
  }
  .site { position: absolute; left: 0; right: 0; top: 210px; text-align: center; font-size: 12.5px; color: var(--brand-blue); }
</style>
</head>
<body>
  <section class="card card--front">
    <div class="band band--top"></div>
    <div class="holder">
      <p class="holder__name">Daniel Harper</p>
      <p class="holder__title">Managing Director</p>
    </div>
    <ul class="contact">
      <li><svg viewBox="0 0 10 10"><path d="M2 0.5l2 2-1 1.2c0.6 1.3 1.5 2.2 2.8 2.8L7 5.5l2 2-1.2 1.7C4.5 9 1 5.5 0.8 1.7z"/></svg>(055)987654321</li>
      <li><svg viewBox="0 0 10 10"><path d="M0 2h10v1L5 6 0 3zM0 4l5 3 5-3v4H0z"/></svg>hello@summitharborgrp.example</li>
      <li><svg viewBox="0 0 10 10"><circle cx="5" cy="5" r="5"/></svg>www.summitharborgrp.example</li>
    </ul>
    <p class="partner partner--gate">The Blue Gate</p>
    <p class="partner partner--ledger">Beacon Ledger</p>
    <div class="band band--bottom"></div>
  </section>

  <section class="card card--back">
    <div class="identity">
      <span class="identity__dot"></span>
      <p class="identity__name">Summit Harbor Group</p>
    </div>
    <p class="site">www.summitharborgrp.example</p>
  </section>
</body>
</html>
```